Flyer Template Design

I have attached 4 files. I would like a design template that could be used across these documents so that they have a common look and feel. The content of the documents is tested and should not be changed significantly. The images can be changed. I have also attache our logo for color compatibility.
Updates

Need extra days to review

Target Market(s)

Wealthy Christian donors

Font styles to use
Serif
Sans Serif

```html
<!DOCTYPE html>
<html lang="en">
<head>
<meta charset="utf-8">
<title>The Homestretch Fund – The Final Lap</title>
<link href="https://fonts.googleapis.com/css2?family=Open+Sans:ital,wght@0,400;0,600;0,700;0,800;1,400;1,600;1,700&display=swap" rel="stylesheet">
<style>
  :root {
    --blue-top: #1b95d4;
    --blue-mid: #1f6fb4;
    --blue-deep: #1d3d7a;
    --green: #9cc83d;
    --green-text: #a4d143;
    --white: #ffffff;
    --ink: #2a2a2a;
    --grey: #555a60;
    --photo-a: #7d8a96;
    --photo-b: #3b5f88;
  }
  * { box-sizing: border-box; margin: 0; padding: 0; }
  html, body { width: 990px; height: 1200px; overflow: hidden; background: #ffffff; }
  .flyer {
    position: relative; width: 990px; height: 1200px; overflow: hidden;
    font-family: "Open Sans", Arial, sans-serif; color: var(--white);
  }
  .flyer__shapes { position: absolute; inset: 0; width: 990px; height: 1200px; }
  .brand {
    position: absolute; left: 44px; top: 66px; display: flex; align-items: center; gap: 22px;
  }
  .brand__mark { width: 92px; height: 92px; background: var(--blue-top); }
  .brand__name {
    font-family: "Open Sans", Arial, sans-serif; font-weight: 400; font-size: 34px;
    line-height: 1.05; letter-spacing: 1px; color: var(--ink); text-transform: uppercase;
    border-left: 2px solid var(--ink); padding-left: 18px;
  }
  .headline {
    position: absolute; left: 40px; top: 315px; font-size: 45px; font-weight: 800;
    letter-spacing: 0.5px; text-transform: uppercase;
  }
  .column { position: absolute; width: 418px; font-size: 14px; line-height: 20px; }
  .column--left { left: 40px; top: 400px; }
  .column--right { left: 545px; top: 368px; }
  .column p { margin-bottom: 14px; }
  .column .lead { font-weight: 700; font-size: 14.5px; text-align: justify; }
  .column em { font-style: italic; }
  .section-title {
    color: var(--green-text); font-style: italic; font-weight: 700; font-size: 15px;
    text-transform: uppercase; margin-top: 4px; margin-bottom: 0;
  }
  .column .highlight { color: var(--green-text); font-style: italic; font-weight: 600; margin-bottom: 4px; }
  .column p.tight { margin-bottom: 14px; }
  .call {
    position: absolute; left: 60px; right: 60px; top: 900px; text-align: center;
  }
  .call__title { font-size: 21px; font-weight: 700; letter-spacing: 0.3px; text-transform: uppercase; margin-bottom: 18px; }
  .call__text { font-size: 14.5px; line-height: 21px; text-align: left; }
  .footer { position: absolute; left: 0; right: 0; top: 1074px; text-align: center; color: var(--grey); }
  .footer__invite { font-style: italic; font-size: 24px; color: var(--ink); margin-bottom: 18px; }
  .footer__contact { font-size: 15px; line-height: 24px; }
  .footer__contact strong { font-weight: 700; }
</style>
</head>
<body>
<main class="flyer">
  <svg class="flyer__shapes" viewBox="0 0 612 790" preserveAspectRatio="none" aria-hidden="false">
    <defs>
      <linearGradient id="panelBlue" x1="0" y1="0" x2="0" y2="1">
        <stop offset="0" stop-color="#1b95d4"/>
        <stop offset="0.5" stop-color="#1f6fb4"/>
        <stop offset="1" stop-color="#1d3d7a"/>
      </linearGradient>
      <linearGradient id="photoTone" x1="0" y1="0" x2="1" y2="1">
        <stop offset="0" stop-color="#9aa5ae"/>
        <stop offset="0.55" stop-color="#6f7f8f"/>
        <stop offset="1" stop-color="#3b5f88"/>
      </linearGradient>
    </defs>
    <rect width="612" height="790" fill="#ffffff"/>
    <polygon points="0,107 612,237 612,589 0,564" fill="url(#panelBlue)"/>
    <polygon points="0,107 217,182 0,150" fill="#2aa6e0" opacity="0.6"/>
    <polygon points="0,564 612,589 612,667 0,697" fill="#9cc83d"/>
    <polygon points="362,0 612,0 612,237 217,182" fill="url(#photoTone)"
             role="img" aria-label="Photo of a marathon runner breaking the finish-line tape with arms raised, crowd and banners behind"/>
  </svg>

  <div class="brand">
    <span class="brand__mark"></span>
    <span class="brand__name">The<br>Homestretch<br>Fund</span>
  </div>

  <h1 class="headline">The Final Lap</h1>

  <section class="column column--left">
    <p class="lead">Every four years, the Olympic Marathon is run through the streets of the host city. The final lap, though, is always run in the Olympic Stadium. At the end of the race, the runners burst into the stadium for the final lap, and the crowd explodes in celebration of a long race well run.</p>
    <p>For 2000 years, the church has been running a Marathon, racing to fulfill Jesus' command to <em>"make disciples of all nations."</em> But now we're nearly done: we've come into the stadium; we're on the final lap. And the heavenly crowd is standing and cheering!</p>
    <h2 class="section-title">The Finish Line</h2>
    <p>Jesus himself defined the finish line when he said, <em>"This gospel of the kingdom will be preached in the whole world as a testimony to all nations, and then the end will come."</em></p>
    <h2 class="section-title">When Will the Race End?</h2>
    <p class="highlight">Jesus said, when the gospel has been proclaimed to "all nations".</p>
  </section>

  <section class="column column--right">
    <p>In the Bible, the word <em>"nations"</em> refers to people groups: groups of people who share a common ethnicity, culture, and language. Amazingly, there are about 12,000 of these "nations" around the world—and Jesus commanded us to make disciples in all of them!</p>
    <p>Today, there are still about 500 people groups around the world have never heard the gospel. Most of these remaining groups are small and located in remote, difficult places. But now that we know who and where they are, by God's grace it is possible for us to engage every one of them with the gospel within the next 3 years.</p>
    <p class="highlight">In other words, after a long race, we're on the final lap!</p>
    <h2 class="section-title">Sprinting to the Finish</h2>
    <p>In his second letter, the Apostle Peter instructs believers <em>"to hasten the coming of the day of God."</em> As the end of the race draws near, he's saying, we should sprint toward the finish line, striving to finish the race as quickly as we can.</p>
  </section>

  <section class="call">
    <h2 class="call__title">You can be part of the sprint to the finish.</h2>
    <p class="call__text">Partner with the Homestretch Fund and finance the missionaries who are taking the gospel for the first time to those last remaining people groups. Your investment will "hasten the coming of the day of God" by accelerating the effort to "make disciples of every nation." In 2018, our partners sent the gospel to 231 people groups in 35 countries.</p>
  </section>

  <footer class="footer">
    <p class="footer__invite">Join us as we invest to make disciples in "all nations" by 2022.</p>
    <p class="footer__contact">To learn more, email Martin Avery at <strong>mavery@homestretchfund.org</strong><br>www.homestretchfund.org</p>
  </footer>
</main>
</body>
</html>
```